BrivoMatex. Lantern for the Steady Growth. Business card

Professional business card for BrivoMatex (Lantern for the Steady Growth)
My rationale: Strategy-> Execution-> Results-> Value that lead to the BrivoMatex name: We put the Lantern for the Steady Growth.
We deliver value to our customers helping them at defining a good strategy (cyan arrow). 90% of well formulated strategies fail due to poor execution so we also consider strategical execution very important (green arrow). Due to the execution we obtain the results (blue arrow). Finally, the results provide feedback to redefine strategy, and the new strategy has to be executed and new results obtained providing new feedback and on and on. It's like a wheel that finally, must create corporate value: value for shareholders, staholders, employees, providers...-

Target Market(s)

CEOs and steering comitees , invewrnent funds

Industry/Entity Type

Business Consultant

Contact Information for Business Card

Tommaso Ferlini
CEO & Founder
tommaso.ferlini@brivomatex.example
Mobile: +34 611.205.938
www.brivomatex.example

Colors

Designer to choose colors to be used in the design.

Requirements
Nice to have
• Nice to hace the words: Strategy, execution, results
• Nice to vave the claim: Lantern for the Steady Growth
• The three colors should be shown:
• cyan for STRATEGY
• green for EXECUTION
• blue for RESULTS
Should not have
• Complete black background

```html
<!DOCTYPE html>
<html lang="en">
<head>
<meta charset="utf-8">
<title>BrivoMatex business card</title>
<link href="https://fonts.googleapis.com/css2?family=Marcellus&family=Open+Sans:wght@400;700&display=swap" rel="stylesheet">
<style>
  :root {
    --cyan: #00aeef;
    --ink: #231f20;
    --navy: #2b3990;
    --paper: #ffffff;
    --icon-grey: #d9d9d9;
    --icon-dark: #3a3a3a;
  }
  html, body {
    margin: 0;
    width: 1200px;
    height: 1200px;
    overflow: hidden;
    background: var(--paper);
  }
  .stage { position: relative; width: 1200px; height: 1200px; }
  .card {
    position: absolute;
    width: 673px;
    height: 427px;
    filter: drop-shadow(4px 6px 6px rgba(0,0,0,0.35));
  }
  .card--front { left: 260px; top: 149px; }
  .card--back  { left: 267px; top: 603px; }
  .fill-cyan { fill: var(--cyan); }
  .fill-ink { fill: var(--ink); }
  .fill-paper { fill: var(--paper); }
  .fill-navy { fill: var(--navy); }
  .person-name { font-family: "Marcellus", serif; font-size: 36px; fill: var(--cyan); }
  .person-role { font-family: "Marcellus", serif; font-size: 20px; fill: var(--ink); }
  .contact-text { font-family: "Open Sans", sans-serif; font-size: 10.5px; fill: var(--cyan); }
  .contact-text--phone { letter-spacing: 1.2px; }
  .contact-icon-disc { fill: var(--icon-grey); stroke: #ffffff; stroke-width: 1.5; }
  .contact-icon-glyph { fill: none; stroke: var(--icon-dark); stroke-width: 1.4; stroke-linecap: round; stroke-linejoin: round; }
  .social-tile { fill: var(--cyan); }
  .brand-name { font-family: "Open Sans", sans-serif; font-weight: 700; font-size: 44px; fill: var(--navy); letter-spacing: -1px; }
  .brand-claim { font-family: "Open Sans", sans-serif; font-size: 10px; fill: var(--cyan); letter-spacing: 0.6px; }
</style>
</head>
<body>
<main class="stage">

  <svg class="card card--front" viewBox="0 0 505 320" aria-label="Business card front">
    <defs>
      <clipPath id="front-shape">
        <path d="M0,0 H480 Q505,0 505,25 V320 H25 Q0,320 0,295 Z"/>
      </clipPath>
    </defs>
    <g clip-path="url(#front-shape)">
      <rect class="fill-cyan" width="505" height="320"/>
      <path class="fill-ink" d="M130,0 H505 V185 C470,255 420,300 340,320 H0 V290 C5,160 50,45 130,0 Z"/>
    </g>

    <text class="person-name" x="487" y="58" text-anchor="end">Tommaso Ferlini</text>
    <rect class="fill-cyan" x="265" y="75" width="240" height="27" rx="13.5"/>
    <rect class="fill-cyan" x="480" y="75" width="25" height="27"/>
    <text class="person-role" x="487" y="96" text-anchor="end">CEO &amp; Founder</text>

    <g class="social-links">
      <rect class="social-tile" x="38" y="179" width="34" height="34"/>
      <circle class="social-tile" cx="102" cy="196" r="17"/>
      <rect class="social-tile" x="133" y="179" width="34" height="34"/>
    </g>

    <g class="contact contact--phone">
      <circle class="contact-icon-disc" cx="45" cy="242" r="11"/>
      <rect class="contact-icon-glyph" x="41" y="235" width="8" height="14" rx="1.5"/>
      <text class="contact-text contact-text--phone" x="72" y="246">+34 611.205.938</text>
    </g>
    <g class="contact contact--web">
      <circle class="contact-icon-disc" cx="210" cy="242" r="11"/>
      <circle class="contact-icon-glyph" cx="210" cy="242" r="6"/>
      <path class="contact-icon-glyph" d="M204,242 H216 M210,236 V248"/>
      <text class="contact-text" x="237" y="246">www.brivomatex.example</text>
    </g>
    <g class="contact contact--email">
      <circle class="contact-icon-disc" cx="45" cy="280" r="11"/>
      <rect class="contact-icon-glyph" x="39" y="276" width="12" height="8"/>
      <path class="contact-icon-glyph" d="M39,276 L45,281 L51,276"/>
      <text class="contact-text" x="72" y="284">tommaso.ferlini@brivomatex.example</text>
    </g>
  </svg>

  <svg class="card card--back" viewBox="0 0 505 320" aria-label="Business card back">
    <rect class="fill-cyan" width="505" height="320"/>
    <path class="fill-paper" d="M150,0 H475 Q505,0 505,30 V130 C480,230 420,290 330,320 H30 Q0,320 0,290 V190 C20,100 70,30 150,0 Z"/>
    <text class="brand-name" x="225" y="200" text-anchor="middle">BrivoMatex</text>
    <text class="brand-claim" x="225" y="224" text-anchor="middle">We put the Lantern for the Steady Growth.</text>
  </svg>

</main>
</body>
</html>
```